Upscale business cards needed for Board of Directors

We need professional business cards created for members of our family business Board of Directors. We would like these relatively simple and straightforward, but also with a unique element to set them apart. Probably stick with neutral and simple colors - white, grey etc. We need space for the traditional elements, including name, title, address, email/phone number. And we will be creating several from this template so it needs to be template that is easy to switch information in and out of.
Business
See description

```html
<!DOCTYPE html>
<html lang="en">
<head>
<meta charset="utf-8">
<title>Harbourline Holdings – Business Cards</title>
<link href="https://fonts.googleapis.com/css2?family=Source+Sans+3:wght@400;600&display=swap" rel="stylesheet">
<style>
  :root {
    --backdrop: #e9e6e1;
    --card-dark: #2a2726;
    --card-light: #ffffff;
    --gold: #b49a6c;
    --ink: #1f1d1c;
    --ink-soft: #2e2c2b;
  }
  * { box-sizing: border-box; margin: 0; padding: 0; }
  html, body {
    width: 1200px;
    height: 900px;
    overflow: hidden;
    background: var(--backdrop);
    font-family: "Source Sans 3", Arial, sans-serif;
  }
  .canvas {
    position: relative;
    width: 1200px;
    height: 900px;
  }
  .card {
    position: absolute;
    width: 600px;
    height: 343px;
    box-shadow: 0 10px 28px rgba(0,0,0,0.18);
  }
  .card--back {
    left: 300px;
    top: 80px;
    background: var(--card-dark);
    display: flex;
    align-items: center;
    justify-content: center;
  }
  .card--front {
    left: 300px;
    top: 477px;
    background: var(--card-light);
  }
  .brand-name {
    font-weight: 600;
    text-transform: uppercase;
    letter-spacing: 0.08em;
    line-height: 1;
  }
  .card--back .brand-name {
    color: var(--gold);
    font-size: 40px;
  }
  .card--front .brand-name {
    position: absolute;
    left: 40px;
    bottom: 46px;
    color: var(--ink);
    font-size: 36px;
  }
  .contact {
    position: absolute;
    left: 330px;
    top: 30px;
    color: var(--ink-soft);
    font-size: 13.5px;
    line-height: 1.35;
  }
  .contact__name {
    color: var(--gold);
    font-size: 20px;
    font-weight: 400;
    line-height: 1.1;
  }
  .contact__title { margin-bottom: 14px; }
  .contact__address { margin-bottom: 12px; }
  .contact__list { list-style: none; }
  .contact__item {
    display: flex;
    align-items: center;
    gap: 9px;
  }
  .contact__icon {
    width: 10px;
    height: 10px;
    flex: none;
    fill: none;
    stroke: var(--gold);
    stroke-width: 1.6;
  }
  .contact__icon--solid { fill: var(--gold); stroke: none; }
</style>
</head>
<body>
<main class="canvas">
  <section class="card card--back" aria-label="Card back">
    <p class="brand-name">Harbourline Holdings</p>
  </section>

  <section class="card card--front" aria-label="Card front">
    <div class="contact">
      <h1 class="contact__name">Daniel Mercer</h1>
      <p class="contact__title">Managing Director</p>
      <p class="contact__address">48 Quayside Road<br>Portsmouth, PO1 3LT.</p>
      <ul class="contact__list">
        <li class="contact__item">
          <svg class="contact__icon contact__icon--solid" viewBox="0 0 10 10" aria-hidden="true">
            <path d="M2 0.5 L3.6 2.6 L2.7 3.6 Q3.8 5.9 6.4 7.3 L7.4 6.4 L9.5 8 L8.3 9.5 Q4.6 9.2 2.1 6.3 Q0.3 4 0.5 1.7 Z"/>
          </svg>
          023-555 0148
        </li>
        <li class="contact__item">
          <svg class="contact__icon contact__icon--solid" viewBox="0 0 10 10" aria-hidden="true">
            <path d="M0.5 2 H9.5 V8.5 H0.5 Z M0.5 2 L5 5.6 L9.5 2" stroke="#fff" stroke-width="0.8"/>
          </svg>
          office@harbourline.co
        </li>
        <li class="contact__item">
          <svg class="contact__icon" viewBox="0 0 10 10" aria-hidden="true">
            <rect x="1" y="4.2" width="5" height="2.6" rx="1.3" transform="rotate(-45 3.5 5.5)"/>
            <rect x="4" y="3.2" width="5" height="2.6" rx="1.3" transform="rotate(-45 6.5 4.5)"/>
          </svg>
          www.harbourline.co
        </li>
      </ul>
    </div>
    <p class="brand-name">Harbourline Holdings</p>
  </section>
</main>
</body>
</html>
```